Need Business Card for our Indian Grocery Store

Industry/Entity Type

Grocery Store

Contact Information for Business Card

Manoj Baweja
Director

Store Locations:

Ashvale
482 Elm Parade
P: 03 9172 5843

Kerrington
613 Carlow Road
P: 03 9238 6014

email: kvtmarts@mailnest.example

Requirements
Must have
• Our logo Colours

```html
<!DOCTYPE html>
<html lang="en">
<head>
<meta charset="utf-8">
<title>KVT Groceries &amp; Spices – Business Card</title>
<link rel="stylesheet" href="https://fonts.googleapis.com/css2?family=Raleway:wght@400;500;700&display=swap">
<style>
  :root {
    --stage: #1f3553;
    --card: #ffffff;
    --pattern-tone: #f2f2f2;
    --brand-red: #e21f26;
    --ink: #1b1b1b;
    --ink-soft: #333333;
    --rule: #4a4a4a;
  }
  * { margin: 0; padding: 0; box-sizing: border-box; }
  html, body {
    width: 1200px; height: 1200px; overflow: hidden;
    background: var(--stage);
    font-family: "Raleway", sans-serif;
    font-variant-numeric: lining-nums;
    color: var(--ink);
  }
  .canvas { position: relative; width: 1200px; height: 1200px; }
  .card {
    position: absolute; left: 240px; width: 720px; height: 418px;
    background: var(--card); border-radius: 32px; overflow: hidden;
  }
  .card--front { top: 142px; }
  .card--back { top: 638px; }

  .brand-pattern {
    position: absolute; inset: 14px 0;
    background: var(--pattern-tone);
  }
  .front-brand {
    position: absolute; left: 0; right: 0; top: 176px;
    display: flex; justify-content: center; align-items: center; gap: 14px;
  }
  .front-brand__mark { width: 34px; height: 34px; background: var(--brand-red); border-radius: 50%; }
  .front-brand__name {
    font-weight: 700; font-size: 46px; color: var(--brand-red); letter-spacing: 0.5px;
  }

  .back-brand {
    position: absolute; right: 56px; top: 66px;
    font-weight: 700; font-size: 44px; color: var(--brand-red); letter-spacing: 1px;
  }
  .person { position: absolute; left: 55px; top: 68px; }
  .person__name { font-size: 29px; font-weight: 500; color: var(--ink); }
  .person__surname { color: var(--brand-red); }
  .person__role { font-size: 16px; margin-top: 6px; color: var(--ink-soft); }

  .locations-title {
    position: absolute; left: 55px; top: 160px; font-size: 20px; color: var(--ink-soft);
  }
  .rule { position: absolute; left: 52px; width: 616px; height: 2px; background: var(--rule); }
  .rule--top { top: 191px; }
  .rule--bottom { top: 309px; height: 1.5px; }

  .store { position: absolute; top: 206px; font-size: 19px; line-height: 26px; color: var(--ink); }
  .store--a { left: 56px; }
  .store--b { left: 442px; }
  .store__row { display: flex; gap: 14px; align-items: flex-start; }
  .store__row + .store__row { margin-top: 8px; align-items: center; }
  .icon { width: 22px; height: 22px; flex: none; margin-top: 2px; }

  .email {
    position: absolute; left: 56px; top: 322px;
    display: flex; gap: 14px; align-items: center; font-size: 19px;
  }
</style>
</head>
<body>
<main class="canvas">

  <section class="card card--front" aria-label="Card front">
    <div class="brand-pattern" role="img" aria-label="Faint repeating brand-name pattern"></div>
    <div class="front-brand">
      <span class="front-brand__mark"></span>
      <span class="front-brand__name">KVT Groceries &amp; Spices</span>
    </div>
  </section>

  <section class="card card--back" aria-label="Card back">
    <div class="person">
      <p class="person__name">Manoj <span class="person__surname">Baweja</span></p>
      <p class="person__role">Director</p>
    </div>
    <p class="back-brand">KVT</p>

    <p class="locations-title">Store Locations</p>
    <div class="rule rule--top"></div>

    <div class="store store--a">
      <div class="store__row">
        <svg class="icon" viewBox="0 0 24 24"><path d="M12 2a7 7 0 0 0-7 7c0 5 7 13 7 13s7-8 7-13a7 7 0 0 0-7-7zm0 9.5A2.5 2.5 0 1 1 12 6.5a2.5 2.5 0 0 1 0 5z" fill="#111"/></svg>
        <p>Ashvale,<br>482 Elm Parade</p>
      </div>
      <div class="store__row">
        <svg class="icon" viewBox="0 0 24 24"><circle cx="12" cy="12" r="10" fill="none" stroke="#111" stroke-width="1.8"/><path d="M9 7l1.8 2.6-1.1 1.2a7 7 0 0 0 3.5 3.5l1.2-1.1L17 15l-1 1.8c-4 0-8.8-4.8-8.8-8.8z" fill="#111"/></svg>
        <p>03 9172 5843</p>
      </div>
    </div>

    <div class="store store--b">
      <div class="store__row">
        <svg class="icon" viewBox="0 0 24 24"><path d="M12 2a7 7 0 0 0-7 7c0 5 7 13 7 13s7-8 7-13a7 7 0 0 0-7-7zm0 9.5A2.5 2.5 0 1 1 12 6.5a2.5 2.5 0 0 1 0 5z" fill="#111"/></svg>
        <p>Kerrington,<br>613 Carlow Road</p>
      </div>
      <div class="store__row">
        <svg class="icon" viewBox="0 0 24 24"><circle cx="12" cy="12" r="10" fill="none" stroke="#111" stroke-width="1.8"/><path d="M9 7l1.8 2.6-1.1 1.2a7 7 0 0 0 3.5 3.5l1.2-1.1L17 15l-1 1.8c-4 0-8.8-4.8-8.8-8.8z" fill="#111"/></svg>
        <p>03 9238 6014</p>
      </div>
    </div>

    <div class="rule rule--bottom"></div>

    <div class="email">
      <svg class="icon" viewBox="0 0 26 20" style="width:26px;height:20px"><rect x="1" y="2" width="24" height="16" fill="#111"/><path d="M1 2l12 9 12-9M1 18l9-8M25 18l-9-8" fill="none" stroke="#fff" stroke-width="1.4"/></svg>
      <p>kvtmarts@mailnest.example</p>
    </div>
  </section>

</main>
</body>
</html>
```